Redesign - Trifold Brochure - Adding new and fresh look.

I have attached what we currently have as a brochure but we need it to be redesigned. The information content is accurate but looking for fresh new design/layout. Please see the images attached. In tif and pdf format. If you need a different format to work please specify and will do my best to upload it.

Target Market(s)

Retail giveaways to educate customers.

Requirements
Must have
• New fresh look

```html
<!DOCTYPE html>
<html lang="en">
<head>
<meta charset="utf-8">
<title>CBD Trifold Brochure – Inside Spread</title>
<link rel="stylesheet" href="https://fonts.googleapis.com/css2?family=Poppins:wght@400;500;600;700&display=swap">
<style>
  :root{
    --backdrop:#c8c8c8;
    --teal:#3e7f94;
    --teal-light:#4f9db5;
    --callout:rgba(86,160,182,0.88);
    --accent:#e7b21d;
    --ink:#22262b;
    --ink-soft:#3a3f45;
    --paper:#eceeef;
    --paper-dark:#d9dcde;
    --white:#ffffff;
  }
  *{box-sizing:border-box;margin:0;padding:0}
  html,body{width:1200px;height:936px;overflow:hidden}
  body{background:var(--backdrop);font-family:"Poppins",sans-serif;position:relative}

  .brochure{position:absolute;left:50px;top:70px;width:1100px;height:797px;background:var(--paper);overflow:hidden}

  /* Left panel */
  .panel-left{position:absolute;left:0;top:0;width:367px;height:797px;background:var(--teal);color:var(--white)}
  .panel-left .photo{height:310px;background:linear-gradient(160deg,#9a9a9a 0%,#5e5e5e 45%,#2e2e2e 100%)}
  .panel-left .content{padding:28px 34px 0 36px}
  .section-title{font-weight:600;font-size:31px;line-height:1.1}
  .rule{width:64px;height:3px;background:var(--accent);margin:14px 0 18px}
  .panel-left p{font-size:12.5px;line-height:1.45;margin-bottom:12px;color:#e8f1f4}
  .uses-title{font-weight:500;font-size:20px;line-height:1.25;margin-top:18px}
  .uses-title + .rule{margin:10px 0 14px}
  .uses{list-style:none}
  .uses li{display:flex;align-items:center;gap:10px;font-size:15px;line-height:1;margin-bottom:9px}
  .uses svg{width:15px;height:15px;flex:none}

  /* Middle + right top */
  .main-title{position:absolute;left:402px;top:80px;font-weight:600;font-size:29px;line-height:1.25;color:var(--ink)}
  .main-title .hl{color:var(--teal-light)}
  .main-title + .rule{position:absolute;left:402px;top:170px;margin:0}
  .intro{position:absolute;left:752px;top:42px;width:334px;font-size:10px;line-height:1.26;color:var(--ink-soft)}

  /* Diagram */
  .diagram{position:absolute;left:367px;top:206px;width:696px;height:482px;border-top-right-radius:22px;overflow:hidden;
    background:radial-gradient(ellipse 230px 200px at 560px 250px,#d9501c 0%,#8a2f1a 45%,transparent 75%),
               radial-gradient(ellipse 150px 280px at 120px 250px,#2f8fa0 0%,#1b4c5a 55%,transparent 85%),
               linear-gradient(120deg,#15222b 0%,#223a44 50%,#2a2422 100%)}
  .diagram svg.links{position:absolute;inset:0}
  .brain-frame{position:absolute;left:433px;top:147px;width:240px;height:223px;border:3px solid #f7d67a;border-radius:26px;box-shadow:0 0 18px rgba(247,170,60,.7)}
  .callout{position:absolute;background:var(--callout);color:var(--white);border-radius:9px;padding:10px 14px;font-size:9.5px;line-height:1.35}

  /* Bottom benefits */
  .benefits-band{position:absolute;left:367px;top:688px;width:318px;height:109px;background:var(--ink)}
  .benefits-band h2{position:absolute;left:32px;top:26px;font-weight:500;font-size:30px;color:var(--white)}
  .benefits-band h2 .hl{color:var(--teal-light)}
  .benefits-band .rule{position:absolute;left:32px;top:78px;margin:0;width:60px}
  .band-notch{position:absolute;left:357px;top:728px;width:0;height:0;border-top:11px solid transparent;border-bottom:11px solid transparent;border-right:11px solid var(--ink)}
  .band-point{position:absolute;left:685px;top:730px;width:0;height:0;border-top:12px solid transparent;border-bottom:12px solid transparent;border-left:12px solid var(--ink);z-index:2}
  .nutrients{position:absolute;top:688px;height:109px;padding:14px 0 0 18px;color:var(--ink)}
  .nutrients.high{left:685px;width:215px;background:#b4c0c6}
  .nutrients.low{left:900px;width:200px;background:var(--paper-dark)}
  .nutrients h3{display:flex;align-items:center;gap:6px;font-weight:600;font-size:14px;margin-bottom:8px}
  .nutrients h3 svg{width:14px;height:14px}
  .nutrients ul{list-style:none}
  .nutrients li{display:flex;align-items:center;gap:7px;font-size:11px;line-height:1;margin-bottom:7px}
  .nutrients li svg{width:11px;height:11px;flex:none}
</style>
</head>
<body>
<div class="brochure">

  <section class="panel-left">
    <div class="photo" role="img" aria-label="Black and white photo of a dropper releasing oil into a small glass flask"></div>
    <div class="content">
      <h2 class="section-title">What is CBD?</h2>
      <div class="rule"></div>
      <p>CBD stands for Canna-bi-dy-all. CBD is one of many compounds called phytocan-nabinoids that is found in various plant species.</p>
      <p>The industrial hemp plant is a plentiful source of CBD. When derived from industrial hemp, CBD with less than 0.03% THC by weight has no psychoactive properties but retains all of its</p>
      <h3 class="uses-title">CBD is commonly used as relief from:</h3>
      <div class="rule"></div>
      <ul class="uses">
        <li><svg viewBox="0 0 16 16"><circle cx="8" cy="8" r="8" fill="#22262b"/><path d="M4.5 8.3l2.3 2.3 4.7-4.9" stroke="#fff" stroke-width="1.8" fill="none"/></svg>Pain</li>
        <li><svg viewBox="0 0 16 16"><circle cx="8" cy="8" r="8" fill="#22262b"/><path d="M4.5 8.3l2.3 2.3 4.7-4.9" stroke="#fff" stroke-width="1.8" fill="none"/></svg>Inflammation</li>
        <li><svg viewBox="0 0 16 16"><circle cx="8" cy="8" r="8" fill="#22262b"/><path d="M4.5 8.3l2.3 2.3 4.7-4.9" stroke="#fff" stroke-width="1.8" fill="none"/></svg>Anxiety</li>
        <li><svg viewBox="0 0 16 16"><circle cx="8" cy="8" r="8" fill="#22262b"/><path d="M4.5 8.3l2.3 2.3 4.7-4.9" stroke="#fff" stroke-width="1.8" fill="none"/></svg>Sleep Disorders</li>
        <li><svg viewBox="0 0 16 16"><circle cx="8" cy="8" r="8" fill="#22262b"/><path d="M4.5 8.3l2.3 2.3 4.7-4.9" stroke="#fff" stroke-width="1.8" fill="none"/></svg>Neurological Disorders</li>
        <li><svg viewBox="0 0 16 16"><circle cx="8" cy="8" r="8" fill="#22262b"/><path d="M4.5 8.3l2.3 2.3 4.7-4.9" stroke="#fff" stroke-width="1.8" fill="none"/></svg>Opiate Dependence</li>
      </ul>
    </div>
  </section>

  <h2 class="main-title"><span class="hl">How Does CBD</span><br>Work In Your Body?</h2>
  <div class="rule"></div>

  <p class="intro">Your body produces certain natural compounds called cannabinoids that are used to regulate functions for your entire body. Inside your body there is a processing network for cannabinoids called your Endo-cannabinioid System. CBD mimics the natural cannabinoids produced by your body and stimulates certain receptors found on the surface of cells in your body that effect your ECS. These cells are mainly located in the central nervous system and the immune system. This reaction caused by the in-troduction of CBD helps balance and maintain and restore your body's natural function.</p>

  <div class="diagram" role="img" aria-label="Illustration of a glowing human body beside a glowing brain over a molecular pattern">
    <svg class="links" viewBox="0 0 696 482">
      <g stroke="#ffffff" stroke-width="1" fill="none" opacity=".8">
        <path d="M190 126H238"/><circle cx="190" cy="126" r="2.5" fill="#fff"/>
        <path d="M190 235H238"/><circle cx="190" cy="235" r="2.5" fill="#fff"/>
        <path d="M165 410H213"/><circle cx="165" cy="410" r="2.5" fill="#fff"/>
        <path d="M400 410L445 385"/>
        <path d="M453 126H433V147"/>
      </g>
    </svg>
    <div class="brain-frame"></div>
    <div class="callout" style="left:238px;top:92px;width:215px">CB2 receptors are predominantly found in the immune system.</div>
    <div class="callout" style="left:238px;top:198px;width:215px">CB1 and CB2 receptors are found on the surface of cells in your body that effect your endo-cannabinoid system.</div>
    <div class="callout" style="left:213px;top:367px;width:187px">CB2 receptors are responsible for the regulation of inflammation which in turn reduces pain.</div>
    <div class="callout" style="left:472px;top:324px;width:178px">CB1 receptors are found primarily in the brain controlling memory processing, motor regulation, appetite, pain sensation, mood, and sleep.</div>
  </div>

  <div class="band-notch"></div>
  <div class="benefits-band">
    <h2><span class="hl">Other</span> Benefits</h2>
    <div class="rule"></div>
  </div>
  <div class="band-point"></div>

  <div class="nutrients high">
    <h3><svg viewBox="0 0 14 14"><circle cx="7" cy="7" r="7" fill="#22262b"/><path d="M7 3.5v7M3.5 7h7" stroke="#fff" stroke-width="1.6"/></svg>High In</h3>
    <ul>
      <li><svg viewBox="0 0 12 12"><path d="M1.5 6.3l3 3 6-6.5" stroke="#3e7f94" stroke-width="2" fill="none"/></svg>Omega 3 and 6 Fatty Acids</li>
      <li><svg viewBox="0 0 12 12"><path d="M1.5 6.3l3 3 6-6.5" stroke="#3e7f94" stroke-width="2" fill="none"/></svg>Vitamins A &amp; E</li>
      <li><svg viewBox="0 0 12 12"><path d="M1.5 6.3l3 3 6-6.5" stroke="#3e7f94" stroke-width="2" fill="none"/></svg>Calcium, Iron &amp; Antioxidants</li>
    </ul>
  </div>
  <div class="nutrients low">
    <h3><svg viewBox="0 0 14 14"><circle cx="7" cy="7" r="7" fill="#22262b"/><path d="M3.5 7h7" stroke="#fff" stroke-width="1.6"/></svg>Low In</h3>
    <ul>
      <li><svg viewBox="0 0 12 12"><path d="M1.5 6.3l3 3 6-6.5" stroke="#e7b21d" stroke-width="2" fill="none"/></svg>Saturated Fats</li>
      <li><svg viewBox="0 0 12 12"><path d="M1.5 6.3l3 3 6-6.5" stroke="#e7b21d" stroke-width="2" fill="none"/></svg>Cholesterol</li>
      <li><svg viewBox="0 0 12 12"><path d="M1.5 6.3l3 3 6-6.5" stroke="#e7b21d" stroke-width="2" fill="none"/></svg>Carbohydrates</li>
    </ul>
  </div>

</div>
</body>
</html>
```